Lumora business card for a plastic surgeon

we need a business card for plastic surgeons that work on a clinic called LUMORA.
we want a clean design and the following informations: name of the doctor, doctor's registration number (called CRM), telephone, address, facebook, instagram.
Colors: white, blue tones, light brown/ coffee

facebook and instagram: lumoraesteticaclinica

Industry/Entity Type

Business

Contact Information for Business Card

clean design

Font styles to use
Serif
Sans Serif
Other font styles liked:
• helvetica light

Colors
cee9f5
85cae6
85abd2
3276b5
cfeae6
cedeed
eaf1f7

Requirements
Must have
• doctor's name
• identification number (called CRM)
• contact (phone, facebook, instagram, address)

```html
<!DOCTYPE html>
<html lang="en">
<head>
<meta charset="utf-8">
<title>Lumora business card</title>
<link href="https://fonts.googleapis.com/css2?family=Lato:wght@300;400;700;900&display=swap" rel="stylesheet">
<style>
  :root {
    --navy: #17365f;
    --navy-deep: #132d52;
    --blue-glow: #1e6fa6;
    --sky: #3fb6dd;
    --ink: #1b2f55;
    --paper: #ffffff;
    --backdrop: #eceae6;
  }
  * { margin: 0; padding: 0; box-sizing: border-box; }
  html, body {
    width: 1200px; height: 880px; overflow: hidden;
    background: var(--backdrop);
    font-family: "Lato", sans-serif;
  }
  .sheet {
    width: 1200px; height: 880px;
    display: flex; align-items: center; justify-content: center; gap: 44px;
  }
  .card {
    position: relative;
    width: 540px; height: 310px;
    overflow: hidden;
    box-shadow: 0 10px 28px rgba(0,0,0,.18);
  }

  /* front: contact side */
  .card-front { background: var(--paper); }
  .front-brand {
    position: absolute; left: 300px; top: 52px;
    display: flex; align-items: center; gap: 10px;
  }
  .brand-dot {
    width: 14px; height: 14px; border-radius: 50%;
    background: var(--sky);
  }
  .front-brand .brand-name {
    font-weight: 300; font-size: 38px; letter-spacing: 6px;
    color: var(--sky);
  }
  .doctor {
    position: absolute; left: 48px; top: 124px;
  }
  .doctor-name {
    font-weight: 900; font-size: 19px; color: var(--ink);
  }
  .doctor-crm {
    font-weight: 400; font-size: 15px; color: var(--sky); margin-top: 1px;
  }
  .name-rule {
    position: absolute; left: 222px; top: 154px;
    width: 282px; height: 2px; background: var(--ink);
  }
  .contacts {
    position: absolute; left: 48px; top: 205px;
    list-style: none;
  }
  .contacts li {
    display: flex; align-items: center; gap: 10px;
    font-size: 15px; color: var(--ink); line-height: 21px;
  }
  .contacts svg { width: 13px; height: 13px; flex: none; }
  .address-band {
    position: absolute; left: 0; bottom: 0;
    width: 100%; height: 44px;
    background: var(--navy);
    display: flex; align-items: center; padding-left: 84px; gap: 10px;
    color: #fff; font-size: 15px;
  }
  .address-band svg { width: 14px; height: 14px; }

  /* back: brand side */
  .card-back {
    background: radial-gradient(circle at 58% 52%, var(--blue-glow) 0%, #1a4f85 22%, var(--navy) 52%, var(--navy-deep) 100%);
    display: flex; align-items: center; justify-content: center;
  }
  .back-brand {
    display: flex; align-items: center; gap: 14px;
  }
  .back-brand .brand-dot { background: #fff; width: 16px; height: 16px; }
  .back-brand .brand-name {
    font-weight: 300; font-size: 54px; letter-spacing: 8px; color: #fff;
  }
</style>
</head>
<body>
<main class="sheet">
  <section class="card card-front" aria-label="Card front with contact details">
    <div class="front-brand">
      <span class="brand-dot"></span>
      <span class="brand-name">LUMORA</span>
    </div>

    <div class="doctor">
      <p class="doctor-name">Dr. Helena Prado</p>
      <p class="doctor-crm">CRM #0000</p>
    </div>
    <div class="name-rule"></div>

    <ul class="contacts">
      <li>
        <svg viewBox="0 0 14 14" aria-hidden="true"><circle cx="7" cy="7" r="6" fill="none" stroke="#3fb6dd" stroke-width="1.2"/><path d="M4.6 4.2c.4-.4.8-.3 1 .1l.5 1c.1.3 0 .5-.2.7l-.3.3c.4.9 1.1 1.6 2 2l.3-.3c.2-.2.5-.3.7-.2l1 .5c.4.2.5.6.1 1-.7.7-1.6.7-2.6.1-1.1-.6-2-1.5-2.6-2.6-.6-1-.6-1.9.1-2.6z" fill="#3fb6dd"/></svg>
        (+01).555 208 314
      </li>
      <li>
        <svg viewBox="0 0 14 14" aria-hidden="true"><circle cx="7" cy="7" r="6" fill="none" stroke="#3fb6dd" stroke-width="1.2"/></svg>
        /lumoraesteticaclinica
      </li>
      <li>
        <svg viewBox="0 0 14 14" aria-hidden="true"><circle cx="7" cy="7" r="6" fill="none" stroke="#3fb6dd" stroke-width="1.2"/></svg>
        /lumoraesteticaclinica
      </li>
    </ul>

    <div class="address-band">
      <svg viewBox="0 0 14 14" aria-hidden="true"><circle cx="7" cy="7" r="7" fill="#fff"/><path d="M3.5 7.2 7 4l3.5 3.2H9.6v3H4.4v-3z" fill="#17365f"/></svg>
      Your Address and Suite #, Zip code, State name here
    </div>
  </section>

  <section class="card card-back" aria-label="Card back with clinic name">
    <div class="back-brand">
      <span class="brand-dot"></span>
      <span class="brand-name">LUMORA</span>
    </div>
  </section>
</main>
</body>
</html>
```